Shopify Design for Back Pain Patch

We need a design for the Shopify-based homepage of the new Vorlixa Spine Pad.

The Vorlixa spine pad absorbs the surface energy produced by your body when you are in pain and redistributes it, reducing your discomfort. It is approximately 5” x 5” in size, with an adhesive backing on one side and a cloth-like exterior that is neutral/light tan in color.

We need a website design that matches our packaging (see attached assets). This includes the blue/orange color scheme and our key messages:

-Natural relief for back pain
-Soothes using your body's natural energy
-Odorless, Gentle, Easy to Use
-Reusable up to 5 days

We are going to be using the Shopify platform for this website, so we'd like the design to be usable with this theme:
http://pliantframe.tovashelf.com/pages/theme-features

We will do all of the coding, but please keep this layout in mind for the design.

Target Market(s)

The Vorlixa Spine Pad is targeted to people suffering from mild to moderate, chronic back pain, but who desire to continue leading active lives.

Industry/Entity Type

Adhesive

Requirements
Must have
• The design needs to have the same look and feel as the packaging for the back patch. Please feel free to use any of the attached assets in your design (doesn't need to be all).
Should not have
• We do not want to see stock photography other than the assets provided.

```html
<!DOCTYPE html>
<html lang="en">
<head>
<meta charset="utf-8">
<title>Vorlixa Spine Pad</title>
<link href="https://fonts.googleapis.com/css2?family=Roboto+Condensed:wght@400;700&family=Roboto:wght@300;400&display=swap" rel="stylesheet">
<style>
:root{
  --blue:#1474bd;
  --blue-dark:#0f64a6;
  --orange:#f7861e;
  --text:#3f3f3f;
  --page:#f5f5f5;
  --panel:#e3e5ea;
  --band:#dcdee6;
  --band-dark:#b3b6c7;
  --white:#ffffff;
}
*{box-sizing:border-box;margin:0;padding:0}
html,body{width:1135px;height:1200px;overflow:hidden}
body{position:relative;background:var(--page);font-family:"Roboto",sans-serif;font-weight:300;color:var(--text)}
.abs{position:absolute}
.cond{font-family:"Roboto Condensed",sans-serif;font-weight:400}

.topbar{left:0;top:0;width:1135px;height:67px;background:var(--blue);color:#cfe3f4}
.welcome{left:148px;top:26px;font-size:13px}
.welcome b{color:var(--white);font-weight:400}
.phone{right:148px;top:15px;font-size:12px;display:flex;align-items:center;gap:5px}
.phone svg{display:block}
.toplinks{right:148px;top:36px;font-size:12px}
.toplinks .on{color:var(--white)}
.toplinks .sep{margin:0 6px}

.logo{left:148px;top:80px;color:var(--orange);font-family:"Roboto Condensed",sans-serif;font-weight:700;line-height:1}
.logo .name{font-size:38px;letter-spacing:-.5px}
.logo .sub{font-size:16px;margin-left:40px;margin-top:2px}

.nav{left:380px;top:94px;width:607px;height:38px;background:var(--blue);border-radius:5px;display:flex;align-items:center;color:var(--white);font-size:13px;overflow:hidden}
.nav .home{background:var(--orange);height:100%;width:68px;display:flex;align-items:center;justify-content:center}
.nav .item{padding:0 0 0 20px}
.nav .bar{padding-left:20px;opacity:.8}

.slider{left:148px;top:157px;width:839px;height:358px;background:var(--white);border:1px solid #e6e6e6}
.hero{left:9px;top:9px;width:534px;height:339px;background:linear-gradient(180deg,#bcd6ec 0%,#e8eef3 45%,#6c7078 75%,#2a2d36 100%)}
.dots{left:486px;top:14px;display:flex;gap:5px}
.dots i{width:9px;height:9px;border-radius:50%;background:var(--blue);display:block}
.dots i:first-child{background:var(--orange)}
.features{left:552px;top:9px;width:276px;height:339px;background:linear-gradient(160deg,#9fd6e6 0%,#f2f1ef 14%,#ece8e3 70%,#d8d3cc 96%,#2b2d33 100%)}
.features h2{position:absolute;left:49px;top:34px;color:var(--blue);font-size:25px;font-weight:400}
.feat{position:absolute;left:31px;width:235px;color:var(--blue);font-size:15.5px;line-height:18px;padding-left:19px;font-weight:300;letter-spacing:.3px}
.feat::before{content:"";position:absolute;left:0;top:5px;width:8px;height:8px;border-radius:50%;background:var(--blue)}
.dotline{position:absolute;left:38px;width:226px;border-top:1px dotted #4a90c8}
.btn{background:var(--blue);color:var(--white);border-radius:8px;width:89px;height:29px;display:flex;align-items:center;justify-content:center;font-family:"Roboto Condensed",sans-serif;font-weight:400;font-size:13px}
.shadow{left:190px;top:515px;width:755px;height:10px;background:radial-gradient(ellipse at top,rgba(0,0,0,.25),rgba(0,0,0,0) 70%)}

.col h3,.sec{color:var(--blue);font-size:19px;font-weight:400;font-family:"Roboto Condensed",sans-serif}
.col{top:542px;width:262px}
.col .photo{margin-top:14px;width:262px;height:140px}
.col p{margin-top:17px;font-size:11px;line-height:15.7px;color:var(--text)}
.col .btn{position:absolute;right:0;top:287px}

.divider{left:148px;top:884px;width:839px;border-top:1px solid #d8d8d8}
.intro{left:148px;top:909px;width:542px}
.intro p{margin-top:10px;font-size:11px;line-height:15.7px;color:var(--text)}
.intro .btn{position:absolute;left:460px;top:122px}
.testi{left:725px;top:909px;width:262px}
.arrows{position:absolute;right:0;top:2px;display:flex;gap:10px}
.arrows span{width:20px;height:20px;display:flex;align-items:center;justify-content:center;background:var(--blue)}
.arrows span:first-child{background:var(--orange)}
.testi .box{position:absolute;top:34px;left:0;width:262px;height:118px;background:var(--panel);padding:20px 12px 0 13px;font-size:11px;line-height:15.7px;color:var(--text)}
.testi .box b{color:var(--blue);font-weight:300}

.infoband{left:0;top:1089px;width:1135px;height:55px;background:var(--band)}
.infotab{left:148px;top:0;height:55px;width:154px}
.infotab span{position:absolute;left:9px;top:16px;color:var(--white);font-size:18px;font-family:"Roboto Condensed",sans-serif}
.footlinks{left:322px;top:20px;font-size:11.5px;color:var(--text)}
.footlinks .sep{margin:0 6px}
.cards{left:777px;top:20px;display:flex;gap:3px}
.cards span{display:flex;align-items:center;justify-content:center;width:33px;height:19px;background:var(--white);border:1px solid #c9ccd6;border-radius:2px;font-size:8px;font-weight:400;color:var(--blue)}
.bottomband{left:0;top:1144px;width:1135px;height:56px;background:var(--band-dark)}
.copy{left:147px;top:22px;font-size:11.5px;color:#3a3a44}
.social{right:148px;top:20px;display:flex;gap:12px;font-size:11px;font-weight:400;color:#1f4f80}
.social span{display:flex;align-items:center;gap:4px}
.social span::before{content:"";width:10px;height:10px;border-radius:2px;background:var(--blue)}
</style>
</head>
<body>

<header class="abs topbar">
  <div class="abs welcome cond">Welcome visitor you can <b>login</b> or <b>create an account.</b></div>
  <div class="abs phone cond">
    <svg width="13" height="13" viewBox="0 0 13 13"><rect width="13" height="13" rx="2" fill="#cfe3f4"/><path d="M4 3.5c.6 0 1 1.8 1 2 0 .5-.8.6-.6 1.1.4.9 1.2 1.7 2.1 2.1.5.2.6-.6 1.1-.6.2 0 2 .4 2 1 0 .8-.8 1.4-1.6 1.4C5.6 10.5 2.5 7.4 2.5 5.1c0-.8.7-1.6 1.5-1.6z" fill="#1474bd"/></svg>
    <span>1-800-555-0147</span>
  </div>
  <div class="abs toplinks cond">Home<span class="sep">|</span><span class="on">Shopping Cart</span><span class="sep">|</span>Check Out</div>
</header>

<div class="abs logo">
  <div class="name">Vorlixa</div>
  <div class="sub">Spine Pad</div>
</div>

<nav class="abs nav cond">
  <span class="home">HOME</span>
  <span class="item">ABOUT US</span><span class="bar">|</span>
  <span class="item">OUR CLIENTS</span><span class="bar">|</span>
  <span class="item">OUR PRODUCT</span><span class="bar">|</span>
  <span class="item">BUY NOW</span><span class="bar">|</span>
  <span class="item">CONTACT &nbsp;US</span>
</nav>

<section class="abs slider">
  <div class="abs hero" role="img" aria-label="Cyclist resting by his bike on a city rooftop, wearing the spine pad on his lower back">
    <div class="abs dots"><i></i><i></i><i></i></div>
  </div>
  <div class="abs features">
    <h2 class="cond">OUR FEATURES</h2>
    <div class="feat" style="top:94px">Natural relief for back pain</div>
    <div class="dotline" style="top:121px"></div>
    <div class="feat" style="top:133px">Soothes using your body's natural energy</div>
    <div class="dotline" style="top:178px"></div>
    <div class="feat" style="top:190px">Odorless, Gentle, Easy to Use</div>
    <div class="dotline" style="top:217px"></div>
    <div class="feat" style="top:229px">Reusable up to 5 days</div>
    <div class="btn" style="position:absolute;left:90px;top:264px">MORE</div>
  </div>
</section>
<div class="abs shadow"></div>

<section class="abs col" style="left:148px">
  <h3>OUR CLIENTS</h3>
  <div class="photo" role="img" aria-label="Woman holding a yoga mat, spine pad on her lower back" style="background:linear-gradient(90deg,#d9d9db,#b9a6a4 45%,#c2487a 75%,#e2e2e4)"></div>
  <p>Lorem Ipsum is simply dummy text of the printing and typesetting industry. Lorem Ipsum has been the industry's standard dummy text ever since the 1500s, when an unknown printer took a galley of type and scrambled it to make a type</p>
  <div class="btn">MORE</div>
</section>

<section class="abs col" style="left:437px">
  <h3>OUR PRODUCTS</h3>
  <div class="photo" role="img" aria-label="Runner stretching against a pillar on an outdoor path" style="background:linear-gradient(180deg,#c9ccd0,#8d8c88 55%,#3b3c40)"></div>
  <p>Lorem Ipsum is simply dummy text of the printing and typesetting industry. Lorem Ipsum has been the industry's standard dummy text ever since the 1500s, when an unknown printer took a galley of type and scrambled it to make a type</p>
  <div class="btn">MORE</div>
</section>

<section class="abs col" style="left:725px">
  <h3>OUR SPECIALITY</h3>
  <div class="photo" role="img" aria-label="Cyclist resting beside his bike with the spine pad on his back" style="background:linear-gradient(180deg,#bcd6ec,#e6ecf1 45%,#6a6e78 75%,#2a2d36)"></div>
  <p>Lorem Ipsum is simply dummy text of the printing and typesetting industry. Lorem Ipsum has been the industry's standard dummy text ever since the 1500s, when an unknown printer took a galley of type and scrambled it to make a type</p>
  <div class="btn">MORE</div>
</section>

<div class="abs divider"></div>

<section class="abs intro">
  <h2 class="sec">WELCOME TO VORLIXA BACK PATH</h2>
  <p>Lorem Ipsum is simply dummy text of the printing and typesetting industry. Lorem Ipsum has been the industry's standard dummy text ever since the 1500s, when an unknown printer took a galley of type and scrambled it to make a type specimen book. It has survived not only five centuries, but also the leap into electronic typesetting, remaining essentially unchanged. It was popularised in the 1960s with the release of Letraset sheets containing Lorem Ipsum passages, and more recently with desktop publishing software like Aldus PageMaker including versions of Lorem Ipsum.</p>
  <div class="btn">MORE</div>
</section>

<section class="abs testi">
  <h2 class="sec">TESTIMONIALS</h2>
  <div class="arrows">
    <span><svg width="8" height="10" viewBox="0 0 8 10"><path d="M6 1L2 5l4 4" stroke="#fff" stroke-width="2" fill="none"/></svg></span>
    <span><svg width="8" height="10" viewBox="0 0 8 10"><path d="M2 1l4 4-4 4" stroke="#fff" stroke-width="2" fill="none"/></svg></span>
  </div>
  <div class="box"><b>DR.Lorem</b> Ipsum is simply dummy text of the printing and typesetting industry. Lorem Ipsum has been the industry's standard dummy text ever since the type and scrambled it to make a type</div>
</section>

<footer>
  <div class="abs infoband">
    <div class="abs infotab">
      <svg width="154" height="55" viewBox="0 0 154 55" style="position:absolute;left:0;top:0"><path d="M0 0H128L154 27.5L128 55H0Z" fill="#1474bd"/></svg>
      <span>INFORMATION</span>
    </div>
    <div class="abs footlinks">About us<span class="sep">|</span>Privecy policy<span class="sep">|</span>Terms and conditions<span class="sep">|</span>Site map<span class="sep">|</span>Contact us</div>
    <div class="abs cards"><span>Paylo</span><span>Maxo</span><span>Cardo</span><span>Verro</span><span>Vesta</span><span>Mondo</span></div>
  </div>
  <div class="abs bottomband">
    <div class="abs copy">2013@ Allright reserved Designed by Northgate Studio</div>
    <div class="abs social"><span>Nexlink</span><span>Frondo</span><span>Chirpa</span></div>
  </div>
</footer>

</body>
</html>
```